Financial services business - Brochure Design

Existing financial services company in Melbourne, Australia needing a brochure design. We have an idea for the type of layout we want, but looking to the designer to help realize it.
We want the brochure to convey how professional we are and for the reader to feel trust and security.
The service this brochure covers is around a concept of Quiet Harvest - i.e. how to get rich without thinking about it.

I've attached two documents:
1) QuietHarvest.doc - this is the content for the brochure with some rough drawings and diagrams. The drawings are only rough ideas of the way I want to represent the content. Please re-draw these but theme them consistently.
2) KMHoldings design(concept).doc - this is another rough design we had drafted up in the past that never went through for design. I've included this as an indication as to how we'd like this done and ideas like emphasising certain phrases on colourful sections or whole blank pages to draw attention to phrases or sentences for the reader.

Specifications:
- Communicate wealth, growth, security/safety and trustworthiness.
- Design to be ready to print professionally.
- Please include some stock imagery as appropriate/ where appropriate.
- Please include soft copy that can be distributed in say for example, *.pdf format.
- Original design files required so we can make alterations if required.

```html
<!DOCTYPE html>
<html lang="en">
<head>
<meta charset="utf-8">
<title>KM Holdings – Overview</title>
<link href="https://fonts.googleapis.com/css2?family=Crimson+Text:wght@400;600;700&family=Open+Sans:wght@400;600&display=swap" rel="stylesheet">
<style>
  :root {
    --brand-blue: #1d5b9e;
    --brand-blue-deep: #16427f;
    --brand-blue-light: #2a74b8;
    --heading-blue: #1f5a99;
    --intro-text: #d6e4f3;
    --body-text: #333333;
    --paper: #ffffff;
    --asphalt-dark: #3a3f46;
    --asphalt-mid: #6b6f74;
    --cape-red: #c42a33;
  }
  * { margin: 0; padding: 0; box-sizing: border-box; }
  html, body { width: 1200px; height: 800px; overflow: hidden; background: var(--paper); }
  .page { position: relative; width: 1200px; height: 800px; overflow: hidden; background: var(--paper); font-family: "Crimson Text", Georgia, serif; color: var(--body-text); }

  .header-band {
    position: absolute; left: 0; top: 0; width: 603px; height: 290px;
    background: linear-gradient(135deg, var(--brand-blue-deep) 0%, var(--brand-blue) 55%, var(--brand-blue-light) 100%);
  }
  .header-rule { position: absolute; left: 0; top: 172px; width: 567px; height: 1px; background: rgba(255,255,255,0.85); }
  .page-title {
    position: absolute; right: 36px; top: 132px;
    font-size: 38px; font-weight: 400; color: #fff; line-height: 1; background: transparent;
  }
  .intro {
    position: absolute; left: 43px; top: 198px; width: 520px;
    font-size: 15.5px; line-height: 26px; color: var(--intro-text);
  }
  .intro .company { font-size: 18px; color: #eef4fb; }
  .header-notch { position: absolute; left: 535px; top: 289px; }

  .philosophy { position: absolute; left: 50px; top: 304px; width: 500px; }
  .philosophy h3 { font-size: 15px; font-weight: 700; color: var(--heading-blue); line-height: 22px; }
  .philosophy p { font-size: 15px; line-height: 24px; }
  .philosophy ul { list-style: none; margin-left: 16px; }
  .philosophy li { font-size: 15px; line-height: 24px; display: flex; align-items: center; gap: 9px; }

  .section { position: absolute; left: 50px; width: 505px; }
  .section h2 { font-size: 19px; font-weight: 400; color: var(--heading-blue); line-height: 24px; }
  .section p { font-size: 14.6px; line-height: 22.7px; text-align: justify; }
  .section.alignment { top: 442px; }
  .section.informed { top: 582px; }

  .hero-photo {
    position: absolute; left: 603px; top: 0; width: 597px; height: 755px;
    background:
      radial-gradient(ellipse 45% 40% at 55% 50%, rgba(196,42,51,0.75) 0%, rgba(196,42,51,0.2) 60%, transparent 80%),
      linear-gradient(160deg, var(--asphalt-mid) 0%, var(--asphalt-dark) 100%);
  }

  .footer-band {
    position: absolute; left: 0; top: 755px; width: 1200px; height: 45px;
    background: linear-gradient(90deg, var(--brand-blue-deep) 0%, var(--brand-blue-light) 50%, var(--brand-blue-deep) 100%);
    display: flex; align-items: center; justify-content: space-between; padding: 0 28px;
    font-family: "Open Sans", Arial, sans-serif; font-size: 15px; color: #fff; letter-spacing: 0.2px;
  }
</style>
</head>
<body>
<div class="page">
  <header class="header-band">
    <div class="header-rule"></div>
    <h1 class="page-title">Overview</h1>
    <p class="intro"><span class="company">KM Holdings Group Pty Ltd (KM Holdings)</span> is a boutique accounting firm based in Melbourne with a strong focus on building long lasting relationships and partnerships with our clients.</p>
  </header>
  <svg class="header-notch" width="26" height="13" viewBox="0 0 26 13" aria-hidden="true"><polygon points="0,0 26,0 13,13" fill="#1f5fa3"/></svg>

  <section class="philosophy">
    <h3>KM Holdings Philosophy</h3>
    <p>At KM Holdings, our philosophies are simple to state:</p>
    <ul>
      <li><svg width="8" height="10" viewBox="0 0 8 10" aria-hidden="true"><polyline points="1.5,1 6,5 1.5,9" fill="none" stroke="#1f5a99" stroke-width="2.2"/></svg>Alignment</li>
      <li><svg width="8" height="10" viewBox="0 0 8 10" aria-hidden="true"><polyline points="1.5,1 6,5 1.5,9" fill="none" stroke="#1f5a99" stroke-width="2.2"/></svg>Informed decision making</li>
    </ul>
  </section>

  <section class="section alignment">
    <h2>Alignment</h2>
    <p>It is vital that the philosophies and values between our clients and ours align. Our clients see eye to eye with us and share a drive for success and building a solid financial foundation for their futures.</p>
  </section>

  <section class="section informed">
    <h2>Informed decision making</h2>
    <p>We firmly believe in educating and consulting our clients to assist them in making informed decisions. Rather than receiving a lengthy document full of technical jargon, our clients are engaged regularly and presented with research, industry insights and expert opinions, empowering them with the ability to make the right investment decisions.</p>
  </section>

  <div class="hero-photo" role="img" aria-label="Photo of a young child in a red superhero cape and mask standing confidently with hands on hips on cracked asphalt"></div>

  <footer class="footer-band">
    <span>WWW.KMHOLDINGS.COM</span>
    <span>WWW.KMHOLDINGS.COM</span>
  </footer>
</div>
</body>
</html>
```